Consulting/Brand Licensing business needs business card

We need a business card created for our IP company, that also does consulting and brand licensing. We would like this card to be vague, as our other business' are in the cannabis industry and this is a non-cannabis touching entity. Perhaps something that hints vaguely at the industry without alerting or possibly offending the receiver.

Target Market(s)

CEOs/Key Decision Makers/Industry Leaders

Contact Information for Business Card

No address, simply list Seattle, WA. Phone: 206-555-0147. Name: Dilan Vesterby // email: Dilan@pulvanixa.com

Colors

Designer to choose colors to be used in the design.

Requirements
Must have
• Logo, Name, Email, Phone number, "Consulting, Licensing and Branding Specialists"
Nice to have
• We would like this to be more professional than playful.

```html
<!DOCTYPE html>
<html lang="en">
<head>
<meta charset="utf-8">
<title>Pulvanixa, Inc — Business Card</title>
<link href="https://fonts.googleapis.com/css2?family=Montserrat:wght@400;600;700&display=swap" rel="stylesheet">
<style>
  :root {
    --accent: #e04e2b;
    --ink: #111111;
    --muted: #3a3a3a;
    --card: #ffffff;
    --backdrop: #e9e7e3;
  }
  * { box-sizing: border-box; margin: 0; padding: 0; }
  html, body { width: 1200px; height: 704px; overflow: hidden; }
  body {
    background: var(--backdrop);
    font-family: "Montserrat", Arial, sans-serif;
    color: var(--ink);
    position: relative;
  }
  .card {
    position: absolute;
    top: 198px;
    width: 530px;
    height: 303px;
    background: var(--card);
    box-shadow: 0 2px 10px rgba(0,0,0,0.12);
    overflow: hidden;
  }
  .card--front { left: 50px; }
  .card--back { left: 620px; }

  .brand { position: absolute; }
  .brand__name {
    color: var(--accent);
    font-weight: 700;
    letter-spacing: 1px;
    line-height: 1;
  }
  .brand__legal {
    color: var(--muted);
    font-weight: 400;
    margin-top: 6px;
  }
  .card--front .brand { left: 36px; top: 40px; }
  .card--front .brand__name { font-size: 32px; }
  .card--front .brand__legal { font-size: 13px; padding-left: 28px; }

  .stripes { position: absolute; left: 0; top: 0; }

  .holder { position: absolute; left: 40px; top: 176px; }
  .holder__name { font-size: 22px; font-weight: 700; line-height: 1; letter-spacing: 0.5px; }
  .holder__role { font-size: 11px; font-weight: 700; margin-top: 3px; letter-spacing: 0.5px; }
  .contact { list-style: none; margin-top: 7px; font-size: 12px; font-weight: 600; }
  .contact li { display: flex; align-items: center; gap: 7px; line-height: 17px; }
  .contact svg { width: 12px; height: 12px; flex: none; }

  .card--back .brand {
    left: 0; right: 0; top: 100px; text-align: center;
  }
  .card--back .brand__name { font-size: 30px; }
  .card--back .brand__legal { font-size: 12px; }
  .tagline {
    position: absolute; left: 0; right: 0; top: 186px;
    text-align: center; font-size: 11px; font-weight: 600;
    letter-spacing: 1px; color: var(--muted);
  }
  .site {
    position: absolute; left: 0; right: 0; top: 238px;
    text-align: center; font-size: 11px; letter-spacing: 3px; color: var(--ink);
  }
</style>
</head>
<body>
  <section class="card card--front">
    <svg class="stripes" width="530" height="303" viewBox="0 0 530 303" aria-hidden="true">
      <g stroke="var(--accent)" stroke-width="4">
        <line x1="395" y1="130" x2="490" y2="130"/>
        <line x1="40" y1="152" x2="500" y2="152"/>
        <line x1="410" y1="174" x2="505" y2="174"/>
      </g>
    </svg>
    <div class="brand">
      <div class="brand__name">PULVANIXA</div>
      <div class="brand__legal">Pulvanixa, Inc</div>
    </div>
    <div class="holder">
      <div class="holder__name">DILAN VESTERBY</div>
      <div class="holder__role">MANAGER</div>
      <ul class="contact">
        <li>
          <svg viewBox="0 0 12 12" aria-hidden="true"><rect x="0.5" y="2.5" width="11" height="7" fill="var(--ink)"/><path d="M0.5 2.5 L6 6.5 L11.5 2.5" fill="none" stroke="#fff" stroke-width="1"/></svg>
          Dilan@pulvanixa.com
        </li>
        <li>
          <svg viewBox="0 0 12 12" aria-hidden="true"><rect x="3" y="0.5" width="6.5" height="11" rx="1" fill="none" stroke="var(--ink)" stroke-width="1.2"/><line x1="5" y1="9.5" x2="7.5" y2="9.5" stroke="var(--ink)"/></svg>
          206-555-0147
        </li>
        <li>
          <svg viewBox="0 0 12 12" aria-hidden="true"><path d="M6 11.5 C3 7.5 2 6 2 4.3 A4 4 0 0 1 10 4.3 C10 6 9 7.5 6 11.5 Z" fill="var(--ink)"/><circle cx="6" cy="4.3" r="1.5" fill="#fff"/></svg>
          Seattle, WA
        </li>
      </ul>
    </div>
  </section>

  <section class="card card--back">
    <div class="brand">
      <div class="brand__name">PULVANIXA</div>
      <div class="brand__legal">Pulvanixa, Inc</div>
    </div>
    <div class="tagline">Consulting, Licensing and Branding Specialists</div>
    <div class="site">www.pulvanixa.com</div>
  </section>
</body>
</html>
```